CREW KLO By Your Side!

need 2 banners to display at our upcoming retreat. we are an orthopedic surgeons office and are having a retreat for our employees (80) Our slogan is CREW KLO...By Your Side! we have a logo that i prefer to be ALL blue (due to the yellow not showing up well) I like using yellow and white with it though or other shades of blue. I would like to reuse the banner later if possible for other events so I dont want it to say "retreat"

Target Market(s)

Patients. Employees

Industry/Entity Type

Office

Font styles to use
Other font styles liked:
• Designer preference- I like clear clean lines

Colors
5e8ec2
faee3f
ffffff

Requirements
Must have
• Running man from logo.
• Blue. Yellow white. Prefer logo to be all blue so it shows up better
• 8 feet long. 3 feet wide.
Nice to have
• Movement. Inspiring image of teamwork or relationship building.
• For more info on us see www.klo2day.example
Should not have
• Don't want word retreat or employees on it

```html
<!DOCTYPE html>
<html lang="en">
<head>
<meta charset="utf-8">
<title>CREW KLO By Your Side!</title>
<link href="https://fonts.googleapis.com/css2?family=Arvo:wght@700&family=Great+Vibes&family=Oswald:wght@300;400;600;700&display=swap" rel="stylesheet">
<style>
  :root {
    --sky-top: #5cc0f7;
    --sky-mid: #2f97ea;
    --sky-deep: #1670d4;
    --navy: #0d4c9c;
    --navy-deep: #0a3f86;
    --brand-blue: #15569f;
    --sun: #faee3f;
    --sun-deep: #f2b81c;
    --white: #ffffff;
    --shadow: rgba(10, 40, 90, 0.55);
  }
  * { box-sizing: border-box; margin: 0; padding: 0; }
  html, body { width: 736px; height: 1200px; overflow: hidden; background: var(--white); }
  .banner {
    position: relative;
    width: 736px;
    height: 1200px;
    overflow: hidden;
    font-family: "Oswald", sans-serif;
    color: var(--white);
  }
  .masthead {
    position: absolute; left: 0; top: 0; width: 736px; height: 115px;
    background: linear-gradient(180deg, #7fd2fb 0%, var(--sky-mid) 55%, var(--sky-deep) 100%);
    border-bottom: 2px solid var(--navy-deep);
  }
  .brand {
    position: absolute; left: 20px; top: 18px;
    display: flex; align-items: center; gap: 10px;
  }
  .brand-name {
    font-family: "Oswald", sans-serif; font-weight: 700;
    font-size: 52px; line-height: 1; letter-spacing: 1px;
    color: var(--brand-blue);
  }
  .brand-dot {
    width: 22px; height: 22px; border-radius: 50%;
    background: var(--brand-blue);
  }
  .slogan {
    position: absolute; right: 16px; top: 34px;
    font-family: "Arvo", serif; font-weight: 700;
    font-size: 33px; line-height: 1;
    color: var(--sun);
    text-shadow: 2px 2px 2px var(--shadow);
  }
  .team-photo {
    position: absolute; left: 0; top: 115px; width: 736px; height: 229px;
    background: linear-gradient(90deg, #6d7480 0%, #9aa3ad 20%, #e9eef3 50%, #a6aeb8 80%, #5a626c 100%);
  }
  .philosophy {
    position: absolute; left: 0; top: 344px; width: 736px; height: 173px;
    background: linear-gradient(180deg, var(--navy) 0%, var(--navy-deep) 100%);
    text-align: center;
  }
  .philosophy-title {
    position: absolute; left: 0; right: 0; top: 12px;
    font-family: "Great Vibes", cursive; font-size: 25px; line-height: 1;
  }
  .philosophy-text {
    position: absolute; left: 0; right: 0; top: 52px;
    font-family: "Great Vibes", cursive; font-size: 19px; line-height: 21px;
  }
  .philosophy-lead {
    position: absolute; left: 0; right: 0; top: 128px;
    font-family: "Great Vibes", cursive; font-size: 20px; line-height: 1;
  }
  .philosophy-lead strong {
    font-family: "Arvo", serif; font-weight: 700; font-size: 18px; letter-spacing: .3px;
  }
  .keys {
    position: absolute; left: 0; top: 517px; width: 736px; height: 683px;
    background: linear-gradient(180deg, var(--sky-top) 0%, #3aa6f0 35%, #2388e4 75%, var(--sky-deep) 100%);
    list-style: none;
  }
  .key {
    position: absolute; left: 30px; width: 690px;
    display: flex; align-items: center; gap: 18px;
  }
  .key-number {
    flex: 0 0 34px; height: 34px; border-radius: 6px;
    background: linear-gradient(180deg, #fff4a0 0%, var(--sun) 40%, var(--sun-deep) 100%);
    border: 1px solid #d89a10;
    color: var(--white); font-weight: 700; font-size: 17px;
    display: flex; align-items: center; justify-content: center;
    text-shadow: 1px 1px 1px rgba(150, 90, 0, .7);
  }
  .key-text {
    font-weight: 300; font-size: 19.5px; line-height: 26px;
  }
  .key-text strong { font-weight: 600; font-size: 21px; }
  .key-final .key-text { font-weight: 600; font-size: 21px; }
</style>
</head>
<body>
<main class="banner">
  <header class="masthead">
    <div class="brand">
      <span class="brand-name">KLO</span>
      <span class="brand-dot"></span>
    </div>
    <h1 class="slogan">CREW KLO...By Your Side!</h1>
  </header>

  <div class="team-photo" role="img" aria-label="Five surgeons in white lab coats standing side by side in the clinic lobby"></div>

  <section class="philosophy">
    <h2 class="philosophy-title">“The Patient Journey” Philosophy</h2>
    <p class="philosophy-text">Our most important goal is patient satisfaction.<br>Patients are the most important people in our business.<br>Let’s face it – without them we would not be here.</p>
    <p class="philosophy-lead">Therefore, please observe the following <strong>PATIENT JOURNEY KEYS:</strong></p>
  </section>

  <ol class="keys">
    <li class="key" style="top:24px"><span class="key-number">1</span><span class="key-text"><strong>PATIENTS</strong> are the most important people in our business, whether we are caring for them in person or over the telephone.</span></li>
    <li class="key" style="top:98px"><span class="key-number">2</span><span class="key-text"><strong>PATIENTS</strong> do not depend on us.&nbsp; We depend on them.</span></li>
    <li class="key" style="top:153px"><span class="key-number">3</span><span class="key-text"><strong>PATIENTS</strong> are not an interruption of our work.&nbsp; They are the purpose for our work.</span></li>
    <li class="key" style="top:201px"><span class="key-number">4</span><span class="key-text"><strong>PATIENTS</strong> favor us with their patronage.&nbsp; We are not doing them a favor by serving them.</span></li>
    <li class="key" style="top:272px"><span class="key-number">5</span><span class="key-text"><strong>PATIENTS</strong> are the most important part of our business.&nbsp; They are not outsiders.</span></li>
    <li class="key" style="top:323px"><span class="key-number">6</span><span class="key-text"><strong>PATIENTS</strong> are not statistics.&nbsp; They are human beings with needs, feeling and emotions like our own.</span></li>
    <li class="key" style="top:395px"><span class="key-number">7</span><span class="key-text"><strong>PATIENTS</strong> are not someone with whom we argue or match wits.</span></li>
    <li class="key" style="top:445px"><span class="key-number">8</span><span class="key-text"><strong>PATIENTS</strong> are people who bring us their needs.&nbsp; It is our job to identify and fill those needs.</span></li>
    <li class="key" style="top:518px"><span class="key-number">9</span><span class="key-text"><strong>PATIENTS</strong> are deserving of the most courteous and attentive experience we can give them.</span></li>
    <li class="key key-final" style="top:586px"><span class="key-number">10</span><span class="key-text">PATIENTS ARE THE LIVELIHOOD OF OUR BUSINESS.</span></li>
  </ol>
</main>
</body>
</html>
```